Responsive Perkline Design

We are seeking web design for a company Perkline. This application will be used by businesses to drive brand loyalty through a customer rewards program. Administrators of the web application will be able to monitor user activity (sign-up/points/purchases etc), view/create rewards points, and manage promotional campaigns. We are open to all color schemes so long as the design is clean and simple. Also, please provide style ideas for graphical representation of promo stats as well as clean design for our data tables. Attached are the wireframes for our application along with a sample application for reference.

Industry/Entity Type

Retail

Coding

Coded - Design and coding required

Number of Pages Required

3 page

Requirements
Must have
• Please include responsive design for tablet and mobile views.

```html
<!DOCTYPE html>
<html lang="en">
<head>
<meta charset="utf-8">
<title>Perkline – Members</title>
<link rel="stylesheet" href="https://fonts.googleapis.com/css2?family=Roboto:wght@400;500;700&display=swap">
<style>
:root{
  --header:#494949;
  --footer:#4a4a4a;
  --side:#f5f6f8;
  --side-line:#e8eaed;
  --blue:#3bb3e0;
  --text:#666;
  --muted:#8a8a8a;
  --line:#e3e3e3;
  --row:#f7f8fa;
  --green:#2dbb22;
  --red:#f23a3a;
  --white:#fff;
  --brand:#dcdcdc;
}
*{box-sizing:border-box;margin:0;padding:0}
html,body{width:1200px;height:934px;overflow:hidden;font-family:"Roboto",sans-serif;color:var(--text);background:var(--white)}
.app{position:relative;width:1200px;height:934px}
.topbar{position:absolute;left:0;top:0;width:1200px;height:84px;background:var(--header)}
.brand{position:absolute;left:19px;top:30px;font-weight:500;font-size:19px;letter-spacing:1px;color:var(--brand)}
.top-search{position:absolute;left:291px;top:24px;width:292px;height:37px;border:1px solid #8a8a8a;border-radius:19px;padding:0 16px;display:flex;align-items:center;justify-content:space-between;font-size:13px;color:#8f8f8f}
.top-nav{position:absolute;top:36px;font-size:12px;font-weight:500;color:#cfcfcf;display:flex;align-items:center;gap:6px}
.sidebar{position:absolute;left:0;top:84px;width:259px;height:781px;background:var(--side)}
.nav-group{position:absolute;left:0;width:259px;border-bottom:2px solid var(--side-line)}
.nav-head{position:absolute;left:19px;font-size:14.5px;font-weight:500;color:#6b6b6b;display:flex;align-items:center;gap:10px}
.nav-sub{position:absolute;left:44px;font-size:13px;color:#8a8a8a}
.nav-sub::before{content:"»";margin-right:7px;color:#aaa}
.main{position:absolute;left:259px;top:84px;width:941px;height:781px}
.page-title{position:absolute;left:36px;top:35px;font-size:21px;font-weight:400;color:#666}
.field-label{position:absolute;font-size:12px;color:#666}
.field{position:absolute;height:40px;border:1px solid var(--line);border-radius:3px;background:var(--white)}
.search-btn{position:absolute;left:878px;top:203px;width:42px;height:40px;background:var(--blue);border-radius:0 3px 3px 0;display:flex;align-items:center;justify-content:center}
.members{position:absolute;left:36px;top:295px;width:884px;border-collapse:collapse;font-size:12.5px}
.members th{background:var(--blue);color:var(--white);font-weight:500;font-size:14px;text-align:left;height:60px;padding-left:20px;border-right:1px solid #6cc7ea}
.members th:last-child{border-right:none}
.members td{height:61px;color:var(--muted);padding-left:20px;border-top:1px solid #ececec;border-right:1px solid #ececec;background:var(--row)}
.members td:first-child{border-left:1px solid #ececec}
.members tr:last-child td{border-bottom:1px solid #e0e0e0}
.members td:nth-child(2){padding-left:9px}
.members td:nth-child(3){padding-left:13px}
.members td.act{padding-left:0;text-align:center}
.btn{display:inline-flex;width:50px;height:33px;border-radius:3px;align-items:center;justify-content:center}
.btn i{width:14px;height:12px;border-radius:4px;background:var(--white)}
.btn-edit{background:var(--green)}
.btn-delete{background:var(--red)}
.footer{position:absolute;left:0;top:865px;width:1200px;height:69px;background:var(--footer);color:var(--white);font-size:13.5px;text-align:center;padding-top:28px}
</style>
</head>
<body>
<div class="app">
  <header class="topbar">
    <div class="brand">PERKLINE</div>
    <div class="top-search">SEARCH
      <svg width="13" height="13" viewBox="0 0 14 14"><circle cx="6" cy="6" r="4.5" fill="none" stroke="#9a9a9a" stroke-width="2"/><path d="M9.5 9.5l3.5 3.5" stroke="#9a9a9a" stroke-width="2"/></svg>
    </div>
    <div class="top-nav" style="left:713px"><svg width="11" height="11" viewBox="0 0 12 12"><circle cx="6" cy="3.5" r="3" fill="#bbb"/><path d="M0 12c0-4 3-6 6-6s6 2 6 6z" fill="#bbb"/></svg>WELCOME SUPER ADMIN</div>
    <div class="top-nav" style="left:917px"><svg width="10" height="11" viewBox="0 0 10 12"><rect x="0" y="5" width="10" height="7" rx="1" fill="#bbb"/><path d="M2.5 5V3.5a2.5 2.5 0 015 0V5" fill="none" stroke="#bbb" stroke-width="1.6"/></svg>CHANGE PASSWORD</div>
    <div class="top-nav" style="left:1098px"><svg width="12" height="11" viewBox="0 0 12 11"><rect x="0.5" y="0.5" width="6" height="10" fill="none" stroke="#bbb"/><path d="M5 5.5h6M9 3l2.5 2.5L9 8" fill="none" stroke="#bbb" stroke-width="1.5"/></svg>SIGN OUT</div>
  </header>

  <aside class="sidebar">
    <div class="nav-group" style="top:0;height:111px"></div>
    <div class="nav-head" style="top:24px"><svg width="14" height="14" viewBox="0 0 14 14"><rect x="1" y="3" width="10" height="10" fill="none" stroke="#777" stroke-width="1.4"/><path d="M5 9l1-3 6-6 2 2-6 6z" fill="#777"/></svg>REGISTRATION</div>
    <div class="nav-sub" style="top:51px">Store Registration</div>
    <div class="nav-sub" style="top:77px">User Registration</div>
    <div class="nav-group" style="top:111px;height:42px"></div>
    <div class="nav-head" style="top:127px"><svg width="14" height="14" viewBox="0 0 14 14"><rect x="1" y="3" width="10" height="10" fill="none" stroke="#777" stroke-width="1.4"/><path d="M5 9l1-3 6-6 2 2-6 6z" fill="#777"/></svg>MEMBER</div>
    <div class="nav-group" style="top:153px;height:44px"></div>
    <div class="nav-head" style="top:170px"><svg width="15" height="12" viewBox="0 0 15 12"><rect x="2" y="1" width="11" height="7" fill="none" stroke="#777" stroke-width="1.4"/><rect x="0" y="9.5" width="15" height="2" fill="#777"/></svg>ACTIVITY</div>
    <div class="nav-group" style="top:197px;height:159px"></div>
    <div class="nav-head" style="top:213px"><svg width="14" height="14" viewBox="0 0 14 14"><path d="M7 1l1.8 4 4.2.4-3.2 2.8 1 4.3L7 10.3 3.2 12.5l1-4.3L1 5.4l4.2-.4z" fill="none" stroke="#777" stroke-width="1.2"/></svg>REWARDS</div>
    <div class="nav-sub" style="top:242px">Add Reward</div>
    <div class="nav-sub" style="top:268px">Add Reward Point</div>
    <div class="nav-sub" style="top:295px">Rewards List</div>
    <div class="nav-sub" style="top:321px">Reward Redeemed</div>
    <div class="nav-group" style="top:356px;height:161px"></div>
    <div class="nav-head" style="top:375px"><svg width="14" height="14" viewBox="0 0 14 14"><path d="M7 1l6 3.5v5L7 13 1 9.5v-5z" fill="none" stroke="#777" stroke-width="1.3"/><path d="M1 4.5l6 3.5 6-3.5M7 8v5" fill="none" stroke="#777" stroke-width="1.2"/></svg>CAMPAIGN</div>
    <div class="nav-sub" style="top:403px">Add Campaign</div>
    <div class="nav-sub" style="top:429px">Show Campaign</div>
    <div class="nav-sub" style="top:456px">Campaign Reached</div>
    <div class="nav-sub" style="top:482px">Campaign Overview</div>
    <div class="nav-group" style="top:517px;height:107px"></div>
    <div class="nav-head" style="top:538px"><svg width="16" height="14" viewBox="0 0 16 14"><circle cx="5" cy="8" r="3.5" fill="none" stroke="#777" stroke-width="2.2" stroke-dasharray="2 1.2"/><circle cx="12" cy="4" r="2.3" fill="none" stroke="#777" stroke-width="1.6" stroke-dasharray="1.5 1"/></svg>SETTING</div>
    <div class="nav-sub" style="top:566px">User Group</div>
    <div class="nav-sub" style="top:592px">User Authorization</div>
    <div class="nav-group" style="top:624px;height:46px"></div>
    <div class="nav-head" style="top:640px"><svg width="13" height="13" viewBox="0 0 13 13"><rect x="1" y="5" width="11" height="7" fill="#777"/><rect x="0" y="3" width="13" height="3" fill="#777"/><rect x="5.7" y="3" width="1.6" height="9" fill="#f5f6f8"/></svg>PROMOTIONS</div>
  </aside>

  <main class="main">
    <h1 class="page-title">MEMBERS</h1>
    <div class="field-label" style="left:38px;top:101px">ALL MEMBERS : 4</div>
    <div class="field-label" style="left:262px;top:101px">NEW : 1</div>
    <div class="field-label" style="left:488px;top:101px">REGULAR : 1</div>
    <div class="field-label" style="left:712px;top:101px">VIP : 1</div>
    <div class="field" style="left:37px;top:119px;width:210px"></div>
    <div class="field" style="left:261px;top:119px;width:210px"></div>
    <div class="field" style="left:487px;top:119px;width:210px"></div>
    <div class="field" style="left:711px;top:119px;width:210px"></div>
    <div class="field-label" style="left:38px;top:185px">SHOW</div>
    <div class="field-label" style="left:490px;top:185px">SEARCH TEXT</div>
    <div class="field" style="left:37px;top:203px;width:432px">
      <svg style="position:absolute;right:13px;top:14px" width="8" height="12" viewBox="0 0 8 12"><path d="M4 0l4 5H0zM4 12L0 7h8z" fill="#555"/></svg>
    </div>
    <div class="field" style="left:489px;top:203px;width:390px"></div>
    <div class="search-btn"><svg width="14" height="14" viewBox="0 0 14 14"><circle cx="6" cy="6" r="4.3" fill="none" stroke="#fff" stroke-width="2"/><path d="M9.3 9.3l3.5 3.5" stroke="#fff" stroke-width="2.2"/></svg></div>

    <table class="members">
      <colgroup><col style="width:112px"><col style="width:97px"><col style="width:96px"><col style="width:97px"><col style="width:97px"><col style="width:97px"><col style="width:96px"><col style="width:97px"><col style="width:95px"></colgroup>
      <thead><tr><th>NAME</th><th>PHONE</th><th>STATUS</th><th>CURRENT</th><th>LIFETIME</th><th>LAST VISIT</th><th>MEMBERS</th><th>EDIT</th><th>DELETE</th></tr></thead>
      <tbody>
        <tr><td>CUSTOMER1</td><td>000-123-1231</td><td>VIP</td><td>65</td><td>987</td><td>01/12/2016</td><td>10/12/2016</td><td class="act"><span class="btn btn-edit"><i></i></span></td><td class="act"><span class="btn btn-delete"><i></i></span></td></tr>
        <tr><td>CUSTOMER1</td><td>000-123-1231</td><td>GOLD</td><td>65</td><td>987</td><td>01/12/2016</td><td>10/12/2016</td><td class="act"><span class="btn btn-edit"><i></i></span></td><td class="act"><span class="btn btn-delete"><i></i></span></td></tr>
        <tr><td>CUSTOMER1</td><td>000-123-1231</td><td>REGULAR</td><td>65</td><td>987</td><td>01/12/2016</td><td>10/12/2016</td><td class="act"><span class="btn btn-edit"><i></i></span></td><td class="act"><span class="btn btn-delete"><i></i></span></td></tr>
        <tr><td>CUSTOMER1</td><td>000-123-1231</td><td>VIP</td><td>65</td><td>987</td><td>01/12/2016</td><td>10/12/2016</td><td class="act"><span class="btn btn-edit"><i></i></span></td><td class="act"><span class="btn btn-delete"><i></i></span></td></tr>
        <tr><td>CUSTOMER1</td><td>000-123-1231</td><td>GOLD</td><td>65</td><td>987</td><td>01/12/2016</td><td>10/12/2016</td><td class="act"><span class="btn btn-edit"><i></i></span></td><td class="act"><span class="btn btn-delete"><i></i></span></td></tr>
        <tr><td>CUSTOMER1</td><td>000-123-1231</td><td>REGULAR</td><td>65</td><td>987</td><td>01/12/2016</td><td>10/12/2016</td><td class="act"><span class="btn btn-edit"><i></i></span></td><td class="act"><span class="btn btn-delete"><i></i></span></td></tr>
      </tbody>
    </table>
  </main>

  <footer class="footer">Copyright © 2016 Perkline. All rights reserved</footer>
</div>
</body>
</html>
```